Vantor Health Group Presentation Folder, for Cancer Awareness, VERY COLORFUL AND MODERN

Presentation Folder I know pretty much what i want so it should be very eazy , I have included files from folders I use now rebrand them to my new company they will be fine, no sense re creating the wheel
Full Bleed Size
20.87" x 16.68"
53 x 42.4 cm
6260 x 5004 pixels
Document Trim Size
20.75" x 16.56"
52.7 x 42.1 cm
6225 x 4969 pixels
Updates

Low design quality

Industry/Entity Type

Medical

Font styles to use
Serif

Colors

Designer to choose colors to be used in the design.

Requirements
Must have
• really I am not looking for some one to redesign, we like our folder front page and would like to see new word information added., there are two folder front pages to choose from
• So Keep the original front page and redesign the back page and the pockets
• Can Make your Design off of one of the ones I already uploaded
Nice to have
• Keep the same color schemes, Keep the original front page and redesign the back page and the pockets
Should not have
• DO not recreate the front covers, use what I gave you and just rebrand

```html
<!DOCTYPE html>
<html lang="en">
<head>
<meta charset="UTF-8">
<title>Vantor Health Group — Presentation Folder Inside Spread</title>
<link href="https://fonts.googleapis.com/css2?family=Raleway:wght@400;500;600&display=swap" rel="stylesheet">
<style>
  :root {
    --bg: #e4e8e8;
    --panel: #f7f9f9;
    --panel-edge: #d3d9d9;
    --pink-strong: #ff86cf;
    --pink-soft: #fccbe6;
    --ink-body: #3b2a63;
    --ink-tag: #4b46d6;
    --brand-ink: #2b3f86;
    --slit: #c9cfd3;
    --white: #ffffff;
  }
  * { box-sizing: border-box; margin: 0; padding: 0; }
  html, body { width: 1200px; height: 1200px; overflow: hidden; }
  body {
    background: var(--bg);
    font-family: "Raleway", sans-serif;
    position: relative;
  }
  .folder-spread {
    position: absolute;
    left: 60px; top: 200px;
    width: 1080px; height: 800px;
    display: flex;
    box-shadow: 0 10px 30px rgba(60, 70, 70, 0.18);
  }
  .folder-panel {
    position: relative;
    width: 540px; height: 800px;
    background: var(--panel);
  }
  .folder-panel--left { border-right: 1px solid var(--panel-edge); }
  .pocket {
    position: absolute;
    bottom: 0;
    width: 540px; height: 300px;
  }
  .pocket--left {
    left: 0;
    background: linear-gradient(100deg, var(--pink-strong) 0%, #fba9da 55%, var(--pink-soft) 100%);
    border-top-right-radius: 22px;
    padding: 52px 44px 0 50px;
    color: var(--ink-body);
  }
  .pocket__body {
    font-size: 14.5px;
    line-height: 1.42;
    font-weight: 500;
  }
  .pocket__tagline {
    display: flex;
    align-items: center;
    gap: 16px;
    margin-top: 26px;
  }
  .ribbon-placeholder {
    flex: 0 0 auto;
    width: 44px; height: 62px;
    border-radius: 10px;
    background: linear-gradient(160deg, #a67be8 0%, #c69ae0 45%, #6fd7ef 100%);
  }
  .pocket__tagline-text {
    font-size: 18.5px;
    line-height: 1.3;
    color: var(--ink-tag);
    font-weight: 400;
  }
  .pocket--right {
    right: 0;
    background: var(--white);
    border-top-left-radius: 22px;
    border-top: 1px solid #eef0f0;
  }
  .card-slits {
    position: absolute;
    left: 130px; top: 60px;
    width: 240px; height: 140px;
  }
  .brand-block {
    position: absolute;
    right: 30px; bottom: 30px;
    text-align: right;
  }
  .brand-name {
    font-weight: 600;
    font-size: 22px;
    color: var(--brand-ink);
  }
  .brand-division {
    margin-top: 8px;
    font-size: 10.5px;
    color: #333a45;
    font-weight: 400;
  }
</style>
</head>
<body>
  <main class="folder-spread">
    <section class="folder-panel folder-panel--left">
      <div class="pocket pocket--left">
        <p class="pocket__body">Hereditary cancer screening provides vital information to help people with a strong personal or family history of cancer understand their own risk of developing the disease. With this information, they can take steps to Potentially Prevent Cancer, Delay the Onset of Cancer or Catch it at an Earlier stage when outcomes and survival rates are Better.</p>
        <div class="pocket__tagline">
          <div class="ribbon-placeholder" role="img" aria-label="Purple and teal cancer awareness ribbon"></div>
          <p class="pocket__tagline-text">Identifying an inherited genetic mutation has the potential to prevent cancer and save lives.</p>
        </div>
      </div>
    </section>
    <section class="folder-panel folder-panel--right">
      <div class="pocket pocket--right">
        <svg class="card-slits" viewBox="0 0 240 140" aria-hidden="true">
          <g stroke="var(--slit)" stroke-width="1.4" fill="none">
            <line x1="0" y1="40" x2="40" y2="0"/>
            <line x1="200" y1="0" x2="240" y2="40"/>
            <line x1="0" y1="100" x2="40" y2="140"/>
            <line x1="200" y1="140" x2="240" y2="100"/>
          </g>
        </svg>
        <div class="brand-block">
          <p class="brand-name">Vantor Health Group</p>
          <p class="brand-division">A division of Meridian Clinical Sales LLC</p>
        </div>
      </div>
    </section>
  </main>
</body>
</html>
```